Breezeway Climate Business Card Design

Design new, 2 sides, business cards for a residential and light commercial heating, air conditioning contractor.

Target Market(s)

Homeowners, small businesses

Industry/Entity Type

Business

Contact Information for Business Card

Dominic Vasquerelli
Phone - 555-214-6837
Email
Address - PO box 618
Millbrook NJ 07999
Website - www.BreezewayClimateLLC.example

Requirements
Must have
• logo, company colors, standard size with no die cut, so I can use printhaven

```html
<!DOCTYPE html>
<html lang="en">
<head>
<meta charset="utf-8">
<title>Breezeway Climate Business Card</title>
<link rel="stylesheet" href="https://fonts.googleapis.com/css2?family=Questrial&family=Montserrat:wght@700&display=swap">
<style>
  :root {
    --stage: #1e1e1e;
    --card-light: #f4f4f4;
    --card-light-edge: #e2e2e2;
    --card-dark: #27304a;
    --card-dark-edge: #1d2439;
    --brand-red: #9b2330;
    --accent-orange: #ee8a2c;
    --text-grey: #5a5a5a;
    --text-light: #e8e9ee;
  }
  * { box-sizing: border-box; margin: 0; padding: 0; }
  html, body { width: 1200px; height: 873px; overflow: hidden; }
  body {
    background: var(--stage);
    font-family: "Questrial", sans-serif;
    position: relative;
  }
  .card {
    position: absolute;
    border-radius: 18px;
    overflow: hidden;
  }
  .card-front {
    left: 80px; top: 210px;
    width: 560px; height: 320px;
    background: linear-gradient(150deg, var(--card-light) 0%, var(--card-light-edge) 100%);
  }
  .card-back {
    left: 730px; top: 148px;
    width: 330px; height: 578px;
    background: linear-gradient(160deg, var(--card-dark) 0%, var(--card-dark-edge) 100%);
  }
  .brand-name {
    position: absolute;
    left: 0; right: 0;
    text-align: center;
    font-family: "Questrial", sans-serif;
    line-height: 1.05;
    letter-spacing: 1px;
    text-transform: uppercase;
  }
  .card-front .brand-name {
    top: 88px;
    font-size: 48px;
    color: var(--brand-red);
  }
  .tagline {
    position: absolute;
    right: 48px; bottom: 42px;
    font-size: 24px;
    letter-spacing: 1.5px;
    color: var(--text-grey);
  }
  .holder {
    position: absolute;
    top: 34px; left: 0; right: 0;
    text-align: center;
  }
  .holder-name {
    font-family: "Montserrat", sans-serif;
    font-weight: 700;
    font-size: 19px;
    color: var(--accent-orange);
  }
  .holder-title {
    margin-top: 4px;
    font-size: 13px;
    letter-spacing: 1px;
    color: var(--text-light);
  }
  .card-back .brand-name {
    top: 168px;
    font-size: 36px;
    color: var(--accent-orange);
  }
  .contacts {
    position: absolute;
    left: 26px; right: 14px; top: 340px;
    list-style: none;
  }
  .contact {
    display: flex;
    align-items: center;
    gap: 14px;
    min-height: 50px;
    font-size: 14.5px;
    line-height: 1.35;
    letter-spacing: 0.3px;
    color: var(--text-light);
    white-space: nowrap;
  }
  .contact svg { width: 30px; height: 30px; flex: none; }
</style>
</head>
<body>
  <section class="card card-front" aria-label="Card front">
    <div class="brand-name">Breezeway<br>Climate</div>
    <p class="tagline">We are just a call away..</p>
  </section>

  <section class="card card-back" aria-label="Card back">
    <div class="holder">
      <div class="holder-name">Dominic Vasquerelli</div>
      <div class="holder-title">Director / Owner</div>
    </div>
    <div class="brand-name">Breezeway<br>Climate</div>
    <ul class="contacts">
      <li class="contact">
        <svg viewBox="0 0 30 30" aria-hidden="true"><rect x="8" y="2" width="14" height="26" rx="2.5" fill="none" stroke="var(--accent-orange)" stroke-width="2"/><line x1="13" y1="24" x2="17" y2="24" stroke="var(--accent-orange)" stroke-width="2"/></svg>
        <span>555-214-6837</span>
      </li>
      <li class="contact">
        <svg viewBox="0 0 30 30" aria-hidden="true"><path d="M15 28 C8 19 6 15 6 11 A9 9 0 0 1 24 11 C24 15 22 19 15 28 Z" fill="var(--accent-orange)"/><circle cx="15" cy="11" r="3.5" fill="var(--card-dark)"/></svg>
        <span>PO box 618<br>Millbrook NJ 07999</span>
      </li>
      <li class="contact">
        <svg viewBox="0 0 30 30" aria-hidden="true"><rect x="2" y="6" width="26" height="18" fill="var(--accent-orange)"/><path d="M2 6 L15 17 L28 6" fill="none" stroke="var(--card-dark)" stroke-width="2"/></svg>
        <span>dominic@breezewayclimate.example</span>
      </li>
      <li class="contact">
        <svg viewBox="0 0 30 30" aria-hidden="true"><circle cx="15" cy="15" r="12" fill="none" stroke="var(--accent-orange)" stroke-width="2.5"/><ellipse cx="15" cy="15" rx="5" ry="12" fill="none" stroke="var(--accent-orange)" stroke-width="2"/><line x1="3" y1="15" x2="27" y2="15" stroke="var(--accent-orange)" stroke-width="2"/></svg>
        <span>www.BreezewayClimateLLC.example</span>
      </li>
    </ul>
  </section>
</body>
</html>
```